quiet meadow therapy (QMT)

I need to build a website for my therapy business.
There are two parts to the website
on the landing page; they choose whether they are therapists making a referral or patients needing more information.
After that, they are taken to their respective pages.
There is the textual information and a referral form on the therapist page, and on the patient page, the text is a bit different, and there will be a booking page on the patient page.
Visually minimal, it's a therapeutic website. I want it clean, clinical, and modern
colors: greenish blue or maybe orangish
PHP/html code
Updates

Hi everyone
I'm very sorry for the lack of responses to your designs. I am trying to work it out, but this platform has been a challenge for me.
I appreciate everyone's efforts, and I am unsure how to rate designs and move forward with the ones I like. There is a 5-star rating, but I don't understand how I'm supposed to politely say that it is not it without feeling like I'm going to affect someone's future rating negatively.
Please understand me. Thank you

Designs look the same

Target Market(s)

therapy and stress management

Industry/Entity Type

stress management therapy

Coding

Coded - Design and coding required

Number of Pages Required

5+ page

Font styles to use
Serif

Colors
0094D4
00A9DD
6FCCEA
C7EBF8
E9F6FB
00AB8E
00BBA5
67D7C9
C6EFE9
E9F9F6

Requirements
Must have
• landing page that that have 2 options. one for therapist another for patient

```html
<!DOCTYPE html>
<html lang="en">
<head>
<meta charset="utf-8">
<title>Quiet Meadow Therapy – Page Designs</title>
<link href="https://fonts.googleapis.com/css2?family=Cinzel:wght@400;600;700&family=Michroma&family=Oswald:wght@300;400;500&family=Raleway:ital,wght@0,400;0,600;1,400&display=swap" rel="stylesheet">
<style>
:root{
  --board:#888888;
  --white:#ffffff;
  --ink:#222222;
  --muted:#555555;
  --blue:#1a4fc4;
  --deep-blue:#0d4f8a;
  --teal:#16738a;
  --green:#3aa54a;
  --green-dark:#2e8f3a;
  --soft-gray:#eeeeee;
  --field:#ffffff;
  --grad-form:linear-gradient(90deg,#3ea447 0%,#1f8570 50%,#0e5f88 100%);
  --grad-btn-green:linear-gradient(90deg,#2e9a3e,#6cc24a);
  --grad-btn-blue:linear-gradient(90deg,#1fa9d6,#1640a8);
  --grad-btn-teal:linear-gradient(90deg,#1a78a8,#3fa84a);
}
*{margin:0;padding:0;box-sizing:border-box}
html,body{width:894px;height:1200px;overflow:hidden}
body{background:var(--board);position:relative;font-family:'Raleway',sans-serif;color:var(--ink)}
.abs{position:absolute}

.board-title{position:absolute;font-family:'Oswald',sans-serif;font-weight:300;color:var(--white);font-size:22px;letter-spacing:.5px;transform:translateX(-50%);white-space:nowrap}

.brand{position:absolute;line-height:1}
.brand-mark{font-family:'Michroma',sans-serif;font-size:13px;color:var(--teal);letter-spacing:1px;display:block}
.brand-tag{font-family:'Oswald',sans-serif;font-weight:500;font-size:3.3px;color:var(--ink);letter-spacing:.1px;display:block;margin-top:1px}

.nav{position:absolute;display:flex;gap:8px;font-size:3.8px;color:var(--ink);white-space:nowrap}
.nav .active{color:var(--green)}
.pill{position:absolute;border-radius:6px;color:var(--white);display:flex;align-items:center;justify-content:center;white-space:nowrap}

/* landing 1 */
.landing-one{left:111px;top:70px;width:306px;height:193px;background:var(--white);overflow:hidden}
.landing-one .nav{font-family:'Raleway',sans-serif;top:19px}
.landing-one .hero{position:absolute;left:0;top:30px;width:306px;height:147px;background:linear-gradient(100deg,#3c3f45 0%,#5a5d62 45%,#4c4f55 100%)}
.landing-one .hero-title{position:absolute;width:100%;text-align:center;font-family:'Cinzel',serif;color:var(--white);font-weight:700;white-space:nowrap}
.landing-one .pill{font-family:'Cinzel',serif;font-size:4.6px;border:1px solid #fff}
.landing-one .foot{position:absolute;left:0;top:177px;width:306px;height:16px;font-family:'Cinzel',serif;font-size:3.6px;text-align:center;line-height:16px;color:var(--muted);border-bottom:1px solid var(--green)}

/* landing 2 */
.landing-two{left:107px;top:325px;width:305px;height:193px;background:var(--white);overflow:hidden;border-top:1px solid var(--green)}
.landing-two .nav{font-family:'Oswald',sans-serif;top:18.5px;text-transform:uppercase;font-size:3.6px;gap:7px}
.landing-two .hero-photo{position:absolute;left:0;top:30px;width:200px;height:144px;background:linear-gradient(90deg,#c9c9c7 0%,#d8d7d3 55%,rgba(255,255,255,0) 100%)}
.landing-two .hero-title{position:absolute;left:177px;font-family:'Michroma',sans-serif;color:#111;line-height:1.05;white-space:nowrap}
.landing-two .pill{font-family:'Oswald',sans-serif;font-size:4px;height:10px}
.landing-two .foot{position:absolute;left:0;top:174px;width:305px;height:19px;background:linear-gradient(90deg,#2a8cbd 0%,#2a8cbd 25%,#46a843 65%);color:var(--white);font-family:'Cinzel',serif;font-size:3.6px;text-align:center;line-height:19px}

/* referral page */
.referral-page{left:480px;top:73px;width:306px;height:1066px;background:var(--white);overflow:hidden}
.referral-page .nav{font-family:'Oswald',sans-serif;top:18.5px;font-size:3.6px;gap:7px}
.ref-hero{position:absolute;left:0;top:27px;width:306px;height:183px;background:linear-gradient(100deg,#2f3d47 0%,#5b6870 40%,#3c4a55 70%,#67747c 100%)}
.ref-hero-title{position:absolute;left:0;top:50px;width:100%;text-align:center;font-family:'Michroma',sans-serif;font-size:7.6px;color:var(--white);line-height:1.3;letter-spacing:.3px}

.section-title{position:absolute;font-family:'Michroma',sans-serif;font-size:8px;color:var(--blue);white-space:nowrap}
.section-title .green{color:var(--green-dark)}
.photo{position:absolute}

.about-copy{position:absolute;left:167px;top:237px;width:115px;font-size:3.1px;line-height:1.85;color:#333}
.btn-small{position:absolute;background:var(--grad-btn-green);color:var(--white);font-family:'Oswald',sans-serif;font-size:3.8px;border-radius:5px;display:flex;align-items:center;justify-content:center}

.service-card{position:absolute;top:415px;width:81px;height:95px;background:var(--white)}
.service-card .photo{left:0;top:0;width:81px;height:47px}
.service-card h3{position:absolute;top:52px;width:100%;text-align:center;font-family:'Oswald',sans-serif;font-weight:400;font-size:3.7px;color:var(--green);line-height:1.4;text-transform:uppercase}
.service-card p{position:absolute;top:69px;left:12px;width:57px;text-align:center;font-size:2.8px;line-height:1.6;color:#444}

.testimonial-title{position:absolute;top:576px;width:100%;text-align:center;font-family:'Michroma',sans-serif;font-size:7.4px;color:var(--white);letter-spacing:.4px}
.arrow-ring{position:absolute;width:11px;height:11px;border:0.8px solid rgba(255,255,255,.7);border-radius:50%}
.quote{position:absolute;left:112px;top:602px;width:140px;font-size:4.4px;font-style:italic;line-height:1.95;color:var(--white)}
.quote-name{position:absolute;left:112px;top:633px;font-family:'Oswald',sans-serif;font-style:italic;font-size:4px;color:var(--white)}

.why-intro{position:absolute;left:36px;top:702px;width:234px;text-align:center;font-size:4.1px;line-height:1.75;color:#333}
.check-item{position:absolute;left:37px;width:120px;font-size:3.5px;line-height:1.6;color:#333;padding-left:14px}
.check-item svg{position:absolute;left:0;top:0}

.form-band{position:absolute;left:0;top:853px;width:306px;height:118px;background:var(--grad-form)}
.form-title{position:absolute;left:25px;top:866px;font-family:'Michroma',sans-serif;font-size:7.4px;color:var(--white);letter-spacing:.4px}
.field{position:absolute;height:8.5px;width:63px;background:var(--field);font-size:3px;color:#555;padding-left:3px;line-height:8.5px}
.submit{position:absolute;left:25px;top:951px;width:31px;height:9px;border-radius:5px;border:0.7px solid #fff;background:var(--grad-btn-blue);color:#fff;font-family:'Michroma',sans-serif;font-size:3.3px;display:flex;align-items:center;justify-content:center}

.footer-head{position:absolute;top:998px;font-family:'Michroma',sans-serif;font-size:3.6px;color:#1b6fd0;letter-spacing:.2px}
.footer-list{position:absolute;top:1007px;font-size:3.3px;color:#333;line-height:7.6px;list-style:none}
.contact-line{position:absolute;font-size:3.3px;color:#333;line-height:1.5}
.social-dot{position:absolute;top:1024px;width:9px;height:9px;border-radius:50%;background:var(--green-dark)}
.copyright{position:absolute;top:1056px;width:100%;text-align:center;font-size:3.6px;color:#333;border-top:0.5px solid #e2e2e2;padding-top:5px}
</style>
</head>
<body>

<div class="board-title" style="left:262px;top:28px">LANDING PAGE SAMPLE1</div>
<div class="board-title" style="left:626px;top:14px">REFERAL PAGE</div>
<div class="board-title" style="left:257px;top:281px">LANDING PAGE SAMPLE2</div>

<!-- Landing page, version one -->
<section class="abs landing-one">
  <div class="brand" style="left:26px;top:6px">
    <span class="brand-mark">QMT</span>
    <span class="brand-tag">QUIET MEADOW THERAPY</span>
  </div>
  <div class="pill" style="left:218px;top:4px;width:62px;height:10px;background:var(--grad-btn-teal);font-family:'Cinzel',serif;font-size:4px">REQUEST CONSULTATION</div>
  <nav class="nav" style="left:119px">
    <span class="active">Home</span><span>About us</span><span>Services</span><span>Our Practitioners</span><span>What to expect</span><span>Contact us</span>
  </nav>
  <div class="hero" role="img" aria-label="Photo of a therapist listening to a client in a softly lit consulting room"></div>
  <div class="hero-title" style="top:74px;font-size:11px;font-weight:600">WELCOME TO QUIET</div>
  <div class="hero-title" style="top:89px;font-size:14.5px">MEADOW THERAPY</div>
  <div class="pill" style="left:79px;top:114px;width:69px;height:12px;background:var(--grad-btn-green)">THERAPIST REFERRAL</div>
  <div class="pill" style="left:152px;top:114px;width:74px;height:12px;background:var(--grad-btn-blue)">MORE INFORMATION</div>
  <div class="foot">COPYRIGHT © 2022 QMT ALL RIGHTS RESERVED.</div>
</section>

<!-- Landing page, version two -->
<section class="abs landing-two">
  <div class="brand" style="left:26px;top:5px">
    <span class="brand-mark">QMT</span>
    <span class="brand-tag">QUIET MEADOW THERAPY</span>
  </div>
  <div class="pill" style="left:218px;top:4px;width:62px;height:10px;background:var(--grad-btn-teal);font-family:'Oswald',sans-serif;font-size:4.2px">REQUEST CONSULTATION</div>
  <nav class="nav" style="left:133px">
    <span class="active">HOME</span><span>ABOUT US</span><span>SERVICES</span><span>OUR PRACTITIONERS</span><span>WHAT TO EXPECT</span><span>CONTACT US</span>
  </nav>
  <div class="hero-photo" role="img" aria-label="Photo of a therapist with a clipboard talking with a seated client on a sofa"></div>
  <div class="hero-title" style="top:64px;font-size:7px">WELCOME TO QUIET</div>
  <div class="hero-title" style="top:75px;font-size:12px">MEADOW</div>
  <div class="hero-title" style="top:91px;font-size:12px">THERAPY</div>
  <div class="pill" style="left:180px;top:112px;width:51px;background:var(--grad-btn-green)">THERAPIST REFERRAL</div>
  <div class="pill" style="left:234px;top:112px;width:48px;background:var(--grad-btn-blue)">MORE INFORMATION</div>
  <div class="foot">COPYRIGHT © 2022 QMT ALL RIGHTS RESERVED.</div>
</section>

<!-- Therapist referral page -->
<section class="abs referral-page">
  <div class="brand" style="left:27px;top:6px">
    <span class="brand-mark">QMT</span>
    <span class="brand-tag">QUIET MEADOW THERAPY</span>
  </div>
  <div class="pill" style="left:232px;top:4px;width:48px;height:10px;background:var(--grad-btn-teal);font-family:'Oswald',sans-serif;font-size:4px">MORE INFORMATION</div>
  <nav class="nav" style="left:147px">
    <span class="active">Home</span><span>About us</span><span>Services</span><span>Our Practitioners</span><span>What to expect</span><span>Contact us</span>
  </nav>

  <div class="ref-hero" role="img" aria-label="Photo of a counsellor comforting a distressed young man in an office"></div>
  <div class="ref-hero-title">LOREM IPSUM DOLOR SIT<br>DO EIUSMOD TEMPOR</div>
  <svg class="abs" style="left:0;top:150px" width="306" height="70" viewBox="0 0 306 70">
    <defs>
      <linearGradient id="heroBand" x1="0" x2="1" y1="0" y2="0">
        <stop offset="0" stop-color="#0d4f8a"/><stop offset="1" stop-color="#1c8a7c"/>
      </linearGradient>
    </defs>
    <path d="M0 36 Q140 -6 306 26 L306 70 L0 70Z" fill="url(#heroBand)"/>
    <path d="M0 58 Q110 4 306 28 L306 70 L0 70Z" fill="#ffffff"/>
  </svg>

  <!-- about -->
  <div class="photo" style="left:25px;top:221px;width:120px;height:99px;border-radius:9px;background:linear-gradient(120deg,#d9d6d2,#ece9e6 60%,#c9b6a6)" role="img" aria-label="Photo of a stressed woman in a mask speaking with a counsellor"></div>
  <div class="section-title" style="left:168px;top:222px">ABOUT US</div>
  <p class="about-copy">We help people ease stress and rebuild balance through calm, evidence based care. Our team listens first, then shapes a plan around you. Sessions are private, unhurried and grounded in trust. Whether you come alone or through a referral, we guide each step with patience and clear goals for lasting change. Reach out today to learn how we can support you or someone in your care.</p>
  <div class="btn-small" style="left:168px;top:307px;width:32px;height:9px">READ MORE</div>

  <!-- services -->
  <svg class="abs" style="left:0;top:322px" width="306" height="300" viewBox="0 0 306 300">
    <path d="M0 120 C110 135 250 90 306 0 L306 300 L0 300Z" fill="#eeeeee"/>
  </svg>
  <div class="section-title" style="left:0;width:100%;text-align:center;top:395px"><span class="green">OUR</span> SERVICES</div>

  <article class="service-card" style="left:25px">
    <div class="photo" style="background:linear-gradient(90deg,#cfc6c4,#e3dcd8 50%,#6b5a52)" role="img" aria-label="Photo of a woman looking out of a winter window"></div>
    <h3>ANXIETY THERAPY &amp;<br>COUNSELLING</h3>
    <p>Gentle support to calm worry and regain steady daily focus.</p>
  </article>
  <article class="service-card" style="left:113px">
    <div class="photo" style="background:linear-gradient(90deg,#5a3a36,#8a6a60 50%,#c8c3c0)" role="img" aria-label="Photo of a worried woman on a leather sofa in session"></div>
    <h3>DEPRESSION COUNSELLING<br>&amp; THERAPY</h3>
    <p>Caring sessions that lift low mood and restore hope again.</p>
  </article>
  <article class="service-card" style="left:199px">
    <div class="photo" style="background:linear-gradient(90deg,#cbc7c2,#b58a3a 50%,#d6d2cd)" role="img" aria-label="Photo of a grieving person sitting with head in hands"></div>
    <h3>GREIF &amp; LOSS THERAPY &amp;<br>COUNSELLING</h3>
    <p>Compassionate guidance through loss, at a pace that feels right.</p>
  </article>

  <!-- testimonials -->
  <svg class="abs" style="left:0;top:535px" width="306" height="133" viewBox="0 0 306 133">
    <defs>
      <linearGradient id="testBand" x1="0" x2="1" y1="0" y2="0">
        <stop offset="0" stop-color="#0c5a8c"/><stop offset=".45" stop-color="#1c7c78"/><stop offset="1" stop-color="#47aa42"/>
      </linearGradient>
    </defs>
    <path d="M0 8 Q153 22 306 0 L306 133 L0 133Z" fill="url(#testBand)"/>
  </svg>
  <div class="testimonial-title">CLIENT TESTIMONIALS</div>
  <div class="arrow-ring" style="left:7px;top:613px"></div>
  <svg class="abs" style="left:7px;top:613px" width="11" height="11" viewBox="0 0 11 11"><path d="M6.3 3.4 L4.3 5.5 L6.3 7.6" stroke="#fff" stroke-width=".8" fill="none"/></svg>
  <div class="arrow-ring" style="left:288px;top:613px"></div>
  <svg class="abs" style="left:288px;top:613px" width="11" height="11" viewBox="0 0 11 11"><path d="M4.7 3.4 L6.7 5.5 L4.7 7.6" stroke="#fff" stroke-width=".8" fill="none"/></svg>
  <div class="abs" style="left:60px;top:599px;width:40px;height:40px;border-radius:50%;border:1.5px solid #fff;background:linear-gradient(180deg,#e9e9e9,#bdbdbd)" role="img" aria-label="Portrait photo of the client giving the testimonial"></div>
  <p class="quote">“Lorem ipsum dolor sit amet, consectetur adipiscing elit, sed do eiusmod tempor incididunt ut labore et dolore magna aliqua. ex ea commodo consequat”.</p>
  <div class="quote-name">_ DANA WHITFIELD</div>

  <!-- why choose us -->
  <div class="section-title" style="left:0;width:100%;text-align:center;top:688px">WHY CHOOSE US</div>
  <p class="why-intro">Lorem ipsum dolor sit amet, consectetur adipiscing elit, sed do eiusmod tempor incididunt ut labore et dolore magna aliqua. Ut enim ad minim veniam, quis nostrud exercitation ullamco laboris nisi ut aliquip ex ea commodo consequat. Duis aute irure dolor in reprehenderit in voluptate velit esse cillum dolore eu fugiat nulla pariatur.</p>

  <div class="check-item" style="top:733px">
    <svg width="10" height="9" viewBox="0 0 10 9"><path d="M1 5 L4 8 L9 1" stroke="#3aa54a" stroke-width="1.3" fill="none"/></svg>
    Lorem ipsum dolor sit amet, consectetur adipiscing elit, sed do eiusmod tempor incididunt ut labore et dolore magna aliqua.
  </div>
  <div class="check-item" style="top:754px">
    <svg width="10" height="9" viewBox="0 0 10 9"><path d="M1 5 L4 8 L9 1" stroke="#3aa54a" stroke-width="1.3" fill="none"/></svg>
    Lorem ipsum dolor sit amet, consectetur adipiscing elit, sed do eiusmod tempor incididunt ut labore et dolore magna aliqua.
  </div>
  <div class="check-item" style="top:775px">
    <svg width="10" height="9" viewBox="0 0 10 9"><path d="M1 5 L4 8 L9 1" stroke="#3aa54a" stroke-width="1.3" fill="none"/></svg>
    Lorem ipsum dolor sit amet, consectetur adipiscing elit, sed do eiusmod tempor incididunt ut labore et dolore magna aliqua.
  </div>
  <div class="check-item" style="top:797px">
    <svg width="10" height="9" viewBox="0 0 10 9"><path d="M1 5 L4 8 L9 1" stroke="#3aa54a" stroke-width="1.3" fill="none"/></svg>
    Lorem ipsum dolor sit amet, consectetur adipiscing elit, sed do eiusmod tempor incididunt ut labore et dolore magna aliqua.
  </div>
  <div class="photo" style="left:167px;top:733px;width:104px;height:84px;background:linear-gradient(135deg,#9fb4a6,#c8cfc4 45%,#6d7a63)" role="img" aria-label="Photo of a group therapy session with children and a counsellor"></div>

  <!-- referral form -->
  <div class="form-band"></div>
  <div class="form-title">REFERRAL FORM</div>
  <div class="field" style="left:25px;top:882px">Name</div>
  <div class="field" style="left:90px;top:882px">Age</div>
  <div class="field" style="left:25px;top:893px">Email Address</div>
  <div class="field" style="left:90px;top:893px">Phone Number</div>
  <div class="field" style="left:25px;top:904px">Gender</div>
  <div class="field" style="left:90px;top:904px">DOB</div>
  <div class="field" style="left:25px;top:915.5px">Relationship With Client</div>
  <div class="field" style="left:90px;top:915.5px">Reason For Referral</div>
  <div class="field" style="left:25px;top:927px;width:128px;height:18px;line-height:7px;padding-top:1px">Message</div>
  <div class="submit">SUBMIT</div>
  <div class="abs" style="left:171px;top:851px;width:120px;height:120px;border-radius:50%;background:#0d4f8a"></div>
  <div class="abs" style="left:175px;top:855px;width:109px;height:109px;border-radius:50%;background:linear-gradient(90deg,#e8ecef,#c9d2da 50%,#6a4a3a)" role="img" aria-label="Photo of a smiling woman talking with a therapist"></div>

  <!-- footer -->
  <div class="brand" style="left:27px;top:998px">
    <span class="brand-mark">QMT</span>
    <span class="brand-tag">QUIET MEADOW THERAPY</span>
  </div>
  <div class="social-dot" style="left:26px" aria-label="Social link"></div>
  <div class="social-dot" style="left:39px" aria-label="Social link"></div>
  <div class="social-dot" style="left:52px" aria-label="Social link"></div>
  <div class="social-dot" style="left:65px" aria-label="Social link"></div>

  <div class="footer-head" style="left:106px">NAVIGATION</div>
  <ul class="footer-list" style="left:106px">
    <li>Home</li><li>About Us</li><li>Our Practitioners</li><li>What To Expect</li><li>Contact Us</li>
  </ul>
  <div class="footer-head" style="left:169px">AWARENESS</div>
  <ul class="footer-list" style="left:169px">
    <li>Choosing a therapist</li><li>Find a therapist</li><li>Types of therapists</li><li>Types of therapies</li><li>Helpfull resources</li>
  </ul>
  <div class="footer-head" style="left:235px">CONTACT US</div>
  <svg class="abs" style="left:235px;top:1008px" width="6" height="7" viewBox="0 0 6 7"><path d="M3 6.8 C1 4.5 0.3 3.4 0.3 2.6 A2.7 2.7 0 0 1 5.7 2.6 C5.7 3.4 5 4.5 3 6.8Z" fill="#2e8f3a"/><circle cx="3" cy="2.6" r="1" fill="#fff"/></svg>
  <div class="contact-line" style="left:245px;top:1007px;width:34px">123 Ipsum dolor sit amet, consectetur adipiscing elit.</div>
  <svg class="abs" style="left:235px;top:1028px" width="6" height="6" viewBox="0 0 6 6"><circle cx="3" cy="3" r="3" fill="#2e8f3a"/><path d="M2 1.6 L2.6 2.6 L2.3 3 Q2.8 3.8 3.2 3.9 L3.6 3.5 L4.5 4.1 L4.1 4.6 Q2.6 4.6 1.5 2.2Z" fill="#fff"/></svg>
  <div class="contact-line" style="left:243px;top:1028px">555 014 2290</div>
  <svg class="abs" style="left:235px;top:1038px" width="6" height="6" viewBox="0 0 6 6"><circle cx="3" cy="3" r="3" fill="#2e8f3a"/><rect x="1.5" y="2" width="3" height="2.1" fill="none" stroke="#fff" stroke-width=".4"/><path d="M1.5 2 L3 3.1 L4.5 2" stroke="#fff" stroke-width=".4" fill="none"/></svg>
  <div class="contact-line" style="left:242px;top:1038px">hello@qmt-care.com</div>

  <div class="copyright">Copyright © 2022 QMT All rights reserved.</div>
</section>

</body>
</html>
```